Brindle Works - Fast, Efficient and Gas Mainteance for Domestic, Commercial and Industrial clients

We are in the process of purchasing a new business and would like to get a new logo and business card.
Business is a gas maintenance business that also does new gas installations.
Has been established since 1988.
Services include:
Install all types of gas appliances & equipment inc. hot water units
Maintain / repair / replace all types of gas appliances & equipment

Target Market(s)

Domestic, Commercial and Industrial clients

Industry/Entity Type

Business

Contact Information for Business Card

admin@brindleworks-example.com.au
07 5981 4726
Brindle Works PTY LTD

Logo Text

Gas Fitting & Plumbing Maintenance Specialists

Font styles to use
Sans Serif

Requirements
Must have
• Logo
• Business name, contact number, email address, web address
• Domestic | Commercial | Industrial Est Since 1988
Nice to have
• Possibly a black card with a flame logo to one side
Should not have
• Spelling errors

```html
<!DOCTYPE html>
<html lang="en">
<head>
<meta charset="utf-8">
<title>Brindle Works – Business Card</title>
<link href="https://fonts.googleapis.com/css2?family=Arimo:wght@400;700&display=swap" rel="stylesheet">
<style>
  :root {
    --backdrop: #e8e3da;
    --card: #ffffff;
    --brand-blue: #0b55a8;
    --tab-blue: #1a9ad9;
    --ink: #111111;
    --muted: #444444;
    --rule: rgba(255,255,255,0.85);
  }
  * { margin: 0; padding: 0; box-sizing: border-box; }
  html, body {
    width: 1200px; height: 1200px; overflow: hidden;
    background: var(--backdrop);
    font-family: "Arimo", Arial, sans-serif;
  }
  .canvas { position: relative; width: 1200px; height: 1200px; }
  .card {
    position: absolute; left: 213px; width: 803px; height: 446px;
    background: var(--card); border-radius: 26px;
    box-shadow: 0 6px 18px rgba(0,0,0,0.12);
    overflow: hidden;
  }
  .card--front { top: 130px; }
  .card--back { top: 637px; }
  .wordmark {
    color: var(--brand-blue); font-weight: 700; letter-spacing: 1px; line-height: 1;
  }
  .card--front .wordmark {
    position: absolute; left: 0; right: 0; top: 176px;
    text-align: center; font-size: 82px;
  }
  .brand-block {
    position: absolute; left: 471px; width: 300px; top: 66px; text-align: center;
  }
  .brand-block .wordmark { font-size: 52px; }
  .brand-block .legal-name {
    margin-top: 12px; font-size: 17.5px; color: var(--ink); word-spacing: 3px; line-height: 1.1;
  }
  .brand-block .sectors {
    margin-top: 10px; font-size: 13.5px; color: var(--muted); line-height: 1.35; letter-spacing: 0.3px;
  }
  .contact-tab {
    position: absolute; left: 0; top: 78px; width: 62px; height: 290px;
    background: var(--tab-blue); border-radius: 0 16px 16px 0;
  }
  .tab-rule {
    position: absolute; left: 19px; width: 43px; height: 1.5px; background: var(--rule);
  }
  .tab-icon {
    position: absolute; left: 30px; width: 24px; height: 24px; fill: #fff;
  }
  .contact-list { list-style: none; position: absolute; left: 82px; top: 0; }
  .contact-list li {
    position: absolute; left: 0; white-space: nowrap;
    font-size: 22.5px; color: var(--ink); line-height: 1; word-spacing: 3px;
  }
</style>
</head>
<body>
<main class="canvas">

  <section class="card card--front" aria-label="Card front">
    <div class="wordmark">BRINDLE</div>
  </section>

  <section class="card card--back" aria-label="Card back">
    <div class="contact-tab">
      <svg class="tab-icon" style="top:58px" viewBox="0 0 24 24" aria-hidden="true"><path d="M12 3 2 12h3v8h5v-5h4v5h5v-8h3z"/></svg>
      <div class="tab-rule" style="top:89px"></div>
      <svg class="tab-icon" style="top:107px" viewBox="0 0 24 24" aria-hidden="true"><path d="M7 2c1 0 1.6.6 2 1.6l1.2 3c.3.8 0 1.6-.6 2.1L8.3 9.8c.9 2.3 2.7 4.3 5 5.5l1.2-1.3c.6-.6 1.4-.8 2.1-.4l2.9 1.4c.9.5 1.300 1.2 1.1 2.1l-.5 2.3c-.2.9-1 1.6-2 1.5C9.8 20.4 3.4 14 3.2 5.4c0-1 .6-1.8 1.5-2z"/></svg>
      <div class="tab-rule" style="top:140px"></div>
      <svg class="tab-icon" style="top:157px" viewBox="0 0 24 24" aria-hidden="true"><path d="M12 2a10 10 0 1 0 5 18.7l-.9-1.6A8.2 8.2 0 1 1 20.2 12v1.2c0 1.2-.7 2-1.6 2s-1.5-.8-1.5-2V7.6h-1.8v1A5 5 0 1 0 16 15.4 3.2 3.2 0 0 0 18.6 17c2 0 3.4-1.6 3.4-3.800V12A10 10 0 0 0 12 2zm0 13.2a3.2 3.2 0 1 1 0-6.4 3.2 3.2 0 0 1 0 6.4z"/></svg>
      <div class="tab-rule" style="top:190px"></div>
      <svg class="tab-icon" style="top:206px" viewBox="0 0 24 24" aria-hidden="true"><path d="M12 2a10 10 0 1 0 0 20 10 10 0 0 0 0-20zm7.9 9h-3.5a15 15 0 0 0-1.3-6.3A8 8 0 0 1 19.9 11zM12 4c.9 1.2 2 3.6 2.3 7H9.7C10 7.6 11.1 5.2 12 4zM8.9 4.7A15 15 0 0 0 7.6 11H4.1a8 8 0 0 1 4.8-6.3zM4.1 13h3.5a15 15 0 0 0 1.3 6.3A8 8 0 0 1 4.1 13zM12 20c-.9-1.2-2-3.6-2.3-7h4.6c-.3 3.4-1.4 5.8-2.3 7zm3.1-.7a15 15 0 0 0 1.3-6.3h3.5a8 8 0 0 1-4.8 6.3z"/></svg>
      <div class="tab-rule" style="top:240px"></div>
    </div>

    <ul class="contact-list">
      <li style="top:135px">Address 01, Address, City.</li>
      <li style="top:184px">07 5981 4726</li>
      <li style="top:234px">admin@brindleworks-example.com.au</li>
      <li style="top:283px">www.brindleworks-example.com.au</li>
    </ul>

    <div class="brand-block">
      <div class="wordmark">BRINDLE</div>
      <div class="legal-name">Brindle Works PTY LTD</div>
      <div class="sectors">Domestic | Commercial | Industrial<br>Est Since 1988</div>
    </div>
  </section>

</main>
</body>
</html>
```